Creative, Modern and Conversion based Web Design

Kolvex Digital has recently launched a new logo and as part of our companies rebranding, we need a new website aimed towards the UK B2B marketplace.

The website needs to deliver a modern and creative website design whilst ensuring the design is tailored towards conversion optimisation.

This site must drive point of contact either from an online form, via a direct telephone call or Skype connection.

Our sales are all offline so the website will be a simple, elegant and stunning information portal.

Kolvex Digital offers Digital Marketing services to companies throughout the UK - our target audiences are companies that turnover a minimum of 3 million pounds a year and as such we need to deliver a professional image that installs confidence in our companies abilities.

We do not like websites that are reliant upon stock photography - we are happy for stock photography to be used in a small way however the site must not look like a template filled with stock photography.

What do we do

We supply digital marketing services to those companies who demand a strong return on investment - our company prides itself on delivering successful campaigns that help establish long-term profitable relationships.

A lot of the information presented on our old site is relevant today however the design sucks. So please use the information on our current website as a foundation for your design content.

I am looking for several page designs including

"Home Page" Desktop Version
"Service Page" Desktop Version
"Blog Page" Desktop Version

"Home Page" Mobile Version
"Service Page" Mobile Version
"Blog Page" Mobile Version

In the 1st instance please only submit a single design for the "Home Page" Desktop Version - those designers that we are impressed with will be asked to complete the other designs before a winner is selected.

I like modern clean fonts - the site needs to welcome the reader and encourage them to absorb the information - not to overload and make them leave.

The site must be designed to naturally fit our companies new logo.

NO TEMPLATES

Target Market(s)

B2b - 3 million turnover and above

Industry/Entity Type

Digital Marketing

Number of Pages Required

3 page

Requirements
Must have
• Blended well with the companies logo
• We need conversion optimisation to be a huge part of the design - we considered a conversation when a potential customer reaches out to use via - web form, telephone or skype
• The current content on the old website fits today's business but the design sucks.
• www.kolvexdigital-example.com
Nice to have
• We need 3 pages (in 2 variants Desktop and Mobile)
• Home Page
• Service Page
• Blog Page
• Please only deliver the "Home Page" desktop version - if we are happy with your design we will aks for the additional pages
Should not have
• No templates and not stock photo heavy design

```html
<!DOCTYPE html>
<html lang="en">
<head>
<meta charset="utf-8">
<title>Kolvex Digital – Services</title>
<link href="https://fonts.googleapis.com/css2?family=Poppins:wght@300;400;500;600&display=swap" rel="stylesheet">
<style>
:root{
  --ink:#111418;
  --body:#6b6f74;
  --green:#3fb01a;
  --green-dark:#2a9b12;
  --sky:#a8dcf7;
  --slate:#6b7c88;
  --panel:#f4f4f4;
  --panel-dark:#e4e4e4;
  --link:#1f6fd1;
  --white:#ffffff;
}
*{margin:0;padding:0;box-sizing:border-box}
html,body{width:1200px;height:1200px;overflow:hidden;background:var(--white)}
body{font-family:'Poppins',sans-serif;position:relative}
.services{position:absolute;top:0;left:0;width:1200px;height:747px}
.service{position:absolute;width:250px;margin-left:-125px;text-align:center}
.service__icon{position:absolute;left:50%;margin-left:-53px;width:106px;height:88px;border-radius:10px;
  background:linear-gradient(135deg,var(--sky) 0%,#d9eef9 45%,var(--slate) 100%)}
.service__title{position:absolute;left:0;right:0;font-size:14px;font-weight:600;letter-spacing:1.6px;color:var(--ink)}
.service__text{position:absolute;left:0;right:0;font-size:11.3px;line-height:14.4px;font-weight:300;color:var(--body)}
.service__btn{position:absolute;left:50%;margin-left:-57px;width:114px;height:36px;line-height:36px;
  background:linear-gradient(90deg,var(--green),var(--green-dark));color:var(--white);
  font-size:11px;font-weight:600;border-radius:2px;text-decoration:none}
.row1 .service__icon{top:32px}.row1 .service__title{top:138px}.row1 .service__text{top:169px}.row1 .service__btn{top:246px}
.row2 .service__icon{top:408px}.row2 .service__title{top:514px}.row2 .service__text{top:545px}.row2 .service__btn{top:621px}

.roi{position:absolute;top:747px;left:0;width:1200px;height:453px;background:var(--panel);overflow:hidden}
.roi__shade{position:absolute;inset:0}
.roi__title{position:absolute;left:176px;top:96px;width:400px;font-size:30px;line-height:35px;font-weight:600;color:var(--ink)}
.roi__text{position:absolute;left:176px;top:268px;width:386px;font-size:13.4px;line-height:19.2px;font-weight:300;color:var(--body)}
.roi__text strong{font-weight:600;color:#555}
.roi__text a{color:var(--link);text-decoration:none}
.partner{position:absolute;left:625px;top:111px;width:400px;height:400px;border-radius:50%;background:var(--white)}
</style>
</head>
<body>
<section class="services">
  <div class="row1">
    <div class="service" style="left:312px">
      <div class="service__icon" role="img" aria-label="Monitor with search bar illustration"></div>
      <h3 class="service__title">ORGANIC SEARCH</h3>
      <p class="service__text">Attract traffic that converts and interacts with your brand through Organic. We im-plement both short-term and long-term campaigns to bolster your success.</p>
      <a class="service__btn" href="#">Know More</a>
    </div>
    <div class="service" style="left:602px">
      <div class="service__icon" role="img" aria-label="Dollar coin illustration"></div>
      <h3 class="service__title">PAID SEARCH</h3>
      <p class="service__text">Drive highly converting traffic to your web-site. Our PPC campaigns are ROI-driven from the start – helping you to scale your business quickly.</p>
      <a class="service__btn" href="#">Know More</a>
    </div>
    <div class="service" style="left:902px">
      <div class="service__icon" role="img" aria-label="Browser window with share symbol illustration"></div>
      <h3 class="service__title">LINK OUTREACH</h3>
      <p class="service__text">The core foundation of any search cam-paign. Our team of link outreachers are the best in the industry. We secure link place-ments that drive rankings.</p>
      <a class="service__btn" href="#">Know More</a>
    </div>
  </div>
  <div class="row2">
    <div class="service" style="left:312px">
      <div class="service__icon" role="img" aria-label="Screen with magnifying glass illustration"></div>
      <h3 class="service__title">UX &amp; CRO</h3>
      <p class="service__text">Let us dig into your analytic channels and identify where we can bolster your conver-sion rates while improving user experience.</p>
      <a class="service__btn" href="#">Know More</a>
    </div>
    <div class="service" style="left:602px">
      <div class="service__icon" role="img" aria-label="Open envelope with letter illustration"></div>
      <h3 class="service__title">EMAIL MARKETING</h3>
      <p class="service__text">Our targeted email marketing campaigns allow you to segment users and deliver custom-tailored campaigns and promo-tions to different demographics.</p>
      <a class="service__btn" href="#">Know More</a>
    </div>
    <div class="service" style="left:902px">
      <div class="service__icon" role="img" aria-label="Globe illustration"></div>
      <h3 class="service__title">SOCIAL MEDIA</h3>
      <p class="service__text">Your followers are your most loyal custom-ers. Let us develop a comprehensive strat-egy that aligns your brand with interests, while driving increased sales.</p>
      <a class="service__btn" href="#">Know More</a>
    </div>
  </div>
</section>

<section class="roi">
  <svg class="roi__shade" width="1200" height="453" viewBox="0 0 1200 453" aria-hidden="true">
    <polygon points="944,0 1200,0 1200,453 790,453" fill="var(--panel-dark)"/>
  </svg>
  <h2 class="roi__title">Do you want to see an enviable ROI on search marketing? It’s possible – you’ve found us.</h2>
  <p class="roi__text">We know and understand the world of business. We know that <strong>ROI is the single most important metric</strong> in the market-ing world. We’ve worked within some of the world’s largest industries – such as finance, insurance, payday loans and health; where achieving above 100% ROI is often impossible. For us, it’s just a challenge that can be overcome. Whether we’re working with you to drive your <a href="#">Pay-Per-Click Market-ing</a>, <a href="#">Organic Search Marketing</a> (SEO), Email Marketing or <a href="#">Lead Filtering &amp; Delivery</a> – we always have your ROI in mind. That’s why we’re known as the ROI driven digital agency.</p>
  <div class="partner">
    <svg width="400" height="400" viewBox="0 0 400 400" role="img" aria-label="Partner certification badge">
      <rect x="63" y="124" width="270" height="93" fill="#fafafa" stroke="#eeeeee"/>
      <rect x="63" y="124" width="25" height="93" fill="#4f7cc4"/>
      <rect x="120" y="150" width="170" height="45" rx="4" fill="#e9ecef"/>
      <rect x="78" y="238" width="110" height="40" rx="4" fill="#eef1f3"/>
      <rect x="212" y="238" width="110" height="40" rx="4" fill="#eef1f3"/>
    </svg>
  </div>
</section>
</body>
</html>
```